Noche de Salsa

We need a poster to promote a party. It is a salsa night at La Tortuga, a fun night out to dance, be with friends and have a few drinks. It is an informal occasion. The drinks will not be expensive and the snack will be typical mexican food.
La Tortuga is a campus for 8 local non-profit organizations but it also has high quality event venues and outdoor areas.
We would like a file for print (11x17") and a digital file for social media.
Enclosed:
- File with poster contents in spanish.
- La Tortuga logo
- Picture of palm trees at La Tortuga (you don't have to include this if another graphic fits best.
- Pic of the outside of the restaurant, where the dancing will take place. The restaurante is right in fron of the beach. THIS PICTURE DOES NOT NECESSARILY NEEDS TO BE PART OF THE POSTER.
- La Tortuga Fact Sheet for context.
Target Market(s)
Men and women from 25 to 50 years old.
American and mexican citizens.
Industry/Entity Type
Non-Profit
Colors
Designer to choose colors to be used in the design.
Look and feel
Each slider illustrates characteristics of the customer's brand and the style your logo design should communicate.

```html
<!DOCTYPE html>
<html lang="es">
<head>
<meta charset="utf-8">
<title>Noche de Salsa · La Tortuga</title>
<link href="https://fonts.googleapis.com/css2?family=Archivo+Black&family=Oswald:wght@500;700&family=Montserrat:wght@500;600;700&display=swap" rel="stylesheet">
<style>
  :root {
    --sunset-orange: #f39a1e;
    --sunset-gold: #ffc94a;
    --dusk-purple: #8a2a8f;
    --dusk-magenta: #c43a9a;
    --palm-dark: #3a1a10;
    --ribbon-red: #c8141c;
    --ribbon-dark: #7d0a0f;
    --ribbon-gold: #f5c400;
    --date-yellow: #ffe21a;
    --salsa-light: #f3d6dc;
    --salsa-mid: #d98a9a;
    --salsa-edge: #6d4a52;
    --satin-white: #f4f4f2;
    --satin-shade: #d6d6d2;
    --leaf-green: #3f8a2a;
    --ink: #2f2f2f;
    --ticket-green: #1f6b45;
    --mic-grey: #8b8f94;
  }
  * { margin: 0; padding: 0; box-sizing: border-box; }
  html, body { width: 900px; height: 1200px; overflow: hidden; background: #ffffff; }
  .poster { position: relative; width: 900px; height: 1200px; overflow: hidden; background: var(--satin-white); }

  .sky {
    position: absolute; inset: 0 0 auto 0; height: 560px;
    background: linear-gradient(160deg, var(--sunset-orange) 0%, var(--sunset-gold) 35%, var(--dusk-magenta) 70%, var(--dusk-purple) 100%);
  }
  .palms-photo {
    position: absolute; left: 0; top: 0; width: 420px; height: 620px;
    background: radial-gradient(ellipse at 40% 40%, rgba(58,26,16,.85), rgba(58,26,16,.35) 60%, rgba(58,26,16,0) 80%);
  }
  .dancers-photo {
    position: absolute; left: 190px; top: 0; width: 450px; height: 430px;
    background: radial-gradient(ellipse at 45% 55%, #f6c08a 0%, #b07a8a 45%, rgba(40,30,40,.85) 75%, rgba(40,30,40,0) 100%);
  }
  .venue-photo {
    position: absolute; left: 637px; top: 150px; width: 263px; height: 206px;
    background: linear-gradient(180deg, #9fb6c8 0%, #6f8a5a 45%, #c55a2e 70%, #e8e4dc 100%);
    border-top: 3px dotted #ffffff; border-bottom: 3px dotted #ffffff;
  }
  .mic {
    position: absolute; top: 475px; width: 88px; height: 350px;
    background: linear-gradient(90deg, #3c3f44, var(--mic-grey) 45%, #e6e8ea 60%, #3c3f44);
    border-radius: 40px 40px 12px 12px;
  }
  .mic--left { left: -8px; }
  .mic--right { right: -8px; }
  .satin {
    position: absolute; left: 0; top: 760px; width: 900px; height: 440px;
    background: linear-gradient(170deg, var(--satin-shade) 0%, var(--satin-white) 30%, #ffffff 55%, var(--satin-shade) 80%, var(--satin-white) 100%);
  }

  .headline { position: absolute; left: 0; top: 400px; width: 900px; height: 400px; }
  .headline svg { display: block; }

  .date-band {
    position: absolute; left: 100px; top: 726px; width: 700px; height: 66px;
    background: linear-gradient(180deg, var(--ribbon-red), var(--ribbon-dark));
    box-shadow: 0 6px 12px rgba(0,0,0,.35);
    font: 700 56px/66px "Oswald", sans-serif; text-align: center; color: #ffffff;
    letter-spacing: 1px;
  }
  .date-band .accent { color: var(--date-yellow); }

  .venue-name {
    position: absolute; left: 0; top: 850px; width: 900px;
    display: flex; justify-content: center; align-items: center; gap: 22px;
    font: 600 88px/1 "Montserrat", sans-serif; color: var(--ink);
  }
  .venue-name .dot { width: 54px; height: 54px; border-radius: 50%; background: var(--leaf-green); }

  .address { position: absolute; left: 0; top: 1000px; width: 900px; text-align: center; color: var(--leaf-green); }
  .address .access {
    display: inline-block; padding: 6px 30px;
    border-top: 3px dotted var(--leaf-green); border-bottom: 3px dotted var(--leaf-green);
    font: 700 28px/1.1 "Montserrat", sans-serif; letter-spacing: 9px; color: var(--ink);
  }
  .address .access span { color: var(--leaf-green); }
  .address .directions { margin-top: 8px; font: 600 22px/1.2 "Oswald", sans-serif; letter-spacing: 1px; color: var(--leaf-green); }
  .address .locality { margin-top: 6px; font: 500 18px/1.2 "Montserrat", sans-serif; color: var(--leaf-green); word-spacing: 4px; }

  .ticket {
    position: absolute; left: 175px; top: 1112px; width: 550px; height: 40px;
    background: var(--ticket-green); color: #ffffff;
    font: 500 22px/40px "Montserrat", sans-serif; text-align: center;
    clip-path: polygon(0 0, 100% 0, 96% 50%, 100% 100%, 0 100%, 4% 50%);
  }
  .ticket strong { font-weight: 700; }
</style>
</head>
<body>
<main class="poster">
  <div class="sky" role="img" aria-label="Sunset sky in orange and purple with light streaks"></div>
  <div class="palms-photo" role="img" aria-label="Silhouetted palm trees against the sunset"></div>
  <div class="dancers-photo" role="img" aria-label="Photo of a couple dancing salsa"></div>
  <div class="venue-photo" role="img" aria-label="Photo of the beachfront restaurant terrace where the dance takes place"></div>
  <div class="satin" role="img" aria-label="White satin fabric background"></div>
  <div class="mic mic--left" role="img" aria-label="Vintage microphone"></div>
  <div class="mic mic--right" role="img" aria-label="Vintage microphone"></div>

  <div class="headline">
    <svg width="900" height="400" viewBox="0 0 900 400">
      <defs>
        <linearGradient id="ribbonFill" x1="0" y1="0" x2="0" y2="1">
          <stop offset="0" stop-color="#e0262c"/>
          <stop offset="1" stop-color="#8f0c12"/>
        </linearGradient>
        <linearGradient id="salsaFill" x1="0" y1="0" x2="0" y2="1">
          <stop offset="0" stop-color="#fbeef0"/>
          <stop offset=".55" stop-color="#e7a9b4"/>
          <stop offset="1" stop-color="#f3d6dc"/>
        </linearGradient>
      </defs>
      <!-- ribbon tails -->
      <polygon points="120,150 215,120 230,190 150,205 170,175" fill="var(--ribbon-dark)"/>
      <polygon points="780,150 685,120 670,190 750,205 730,175" fill="var(--ribbon-dark)"/>
      <!-- ribbon body -->
      <path d="M200 70 Q450 0 700 70 L690 150 Q450 85 210 150 Z" fill="url(#ribbonFill)" stroke="var(--ribbon-gold)" stroke-width="4"/>
      <text x="450" y="128" text-anchor="middle" font-family="Archivo Black, sans-serif" font-size="62" fill="#ffffff" stroke="#8f0c12" stroke-width="2" textLength="390" lengthAdjust="spacingAndGlyphs">NOCHE DE</text>
      <!-- big word with extruded depth -->
      <text x="452" y="318" text-anchor="middle" font-family="Archivo Black, sans-serif" font-size="215" fill="var(--salsa-edge)" textLength="640" lengthAdjust="spacingAndGlyphs">Salsa</text>
      <text x="448" y="312" text-anchor="middle" font-family="Archivo Black, sans-serif" font-size="215" fill="#8e6a72" textLength="640" lengthAdjust="spacingAndGlyphs">Salsa</text>
      <text x="444" y="306" text-anchor="middle" font-family="Archivo Black, sans-serif" font-size="215" fill="url(#salsaFill)" stroke="#ffffff" stroke-width="2" textLength="640" lengthAdjust="spacingAndGlyphs">Salsa</text>
    </svg>
  </div>

  <div class="date-band"><span class="accent">VIERNES</span> 14 DE NOVIEMBRE <span class="accent">2014</span></div>

  <div class="venue-name"><span class="dot"></span>La Tortuga</div>

  <div class="address">
    <div class="access"><span>ACCESO</span> COSTERA #1450</div>
    <div class="directions">(AL FINAL DE LA CALLE PALMAR, EN LA ANTIGUA BODEGA)</div>
    <div class="locality">COL. LAS DUNAS • C.P. 23100 • PUERTO SOL, B.C.S</div>
  </div>

  <div class="ticket">ENTRADA: <strong>$100 PESOS</strong> // INCLUYE <strong>1 BEBIDA</strong></div>
</main>
</body>
</html>
```